Bramblewick Gardening Services. A6 flyer single sided

Need an A6 flyer designing. Single sided.
I am a gardener.
I do lawn mowing - one-off garden tidy ups or regular fortnightly visits.
All kinds of trees expertly felled, topped or pruned.
Hedge cutting.
Fencing replaced or repaired.
Fully insured.
Access to fully qualified and licenced tree arborist
07724 316048 or 01632 742918.

I have attached my business card and letter head logo.
I'm open to new designs without incorporating any of my artwork.

Industry/Entity Type

Gardener

```html
<!DOCTYPE html>
<html lang="en">
<head>
<meta charset="utf-8">
<title>Bramblewick Gardening Services – A6 Flyer</title>
<link href="https://fonts.googleapis.com/css2?family=Anton&family=Jost:wght@600;700&display=swap" rel="stylesheet">
<style>
  :root {
    --sky-top: #3f8fe0;
    --sky-bottom: #a9d4f7;
    --hedge-dark: #1f4a12;
    --hedge-mid: #3f7d1d;
    --hedge-light: #7fb83a;
    --leaf-green: #5fae1e;
    --leaf-deep: #2f7a12;
    --soil-brown: #5b3b17;
    --white: #ffffff;
  }
  * { box-sizing: border-box; margin: 0; padding: 0; }
  html, body { width: 1200px; height: 866px; overflow: hidden; background: var(--white); }
  .flyer {
    position: relative;
    width: 1200px;
    height: 866px;
    overflow: hidden;
    background: linear-gradient(180deg, var(--sky-top) 0%, var(--sky-bottom) 62%);
    font-family: "Jost", "Futura", sans-serif;
    color: var(--white);
  }
  .hedge-photo {
    position: absolute;
    left: 0; top: 505px;
    width: 1200px; height: 240px;
    background: linear-gradient(180deg, rgba(127,184,58,0) 0%, var(--hedge-light) 14%, var(--hedge-mid) 45%, var(--hedge-dark) 100%);
  }
  .brand-block {
    position: absolute;
    left: 63px; top: 66px;
    width: 339px; height: 434px;
  }
  .brand-art {
    width: 100%; height: 374px;
    background: radial-gradient(circle at 50% 55%, var(--leaf-green) 0%, var(--leaf-deep) 75%);
  }
  .brand-name {
    height: 60px;
    background: var(--soil-brown);
    display: flex; align-items: center; justify-content: center;
    font-family: "Jost", sans-serif;
    font-weight: 700;
    font-size: 34px;
    letter-spacing: 1px;
    color: var(--white);
  }
  .headline {
    position: absolute;
    left: 441px; top: 52px;
    width: 720px;
    font-family: "Anton", "Impact", sans-serif;
    font-weight: 400;
    font-size: 60px;
    line-height: 70px;
    letter-spacing: 0.2px;
  }
  .services {
    position: absolute;
    top: 210px;
    list-style: none;
    font-weight: 600;
    font-size: 29px;
    line-height: 42px;
  }
  .services li { padding-left: 26px; text-indent: -26px; }
  .services li::before { content: "•"; display: inline-block; width: 26px; text-indent: 0; }
  .services-left { left: 441px; width: 340px; }
  .services-right { left: 797px; width: 360px; }
  .contact-bar {
    position: absolute;
    left: 0; top: 744px;
    width: 1200px; height: 122px;
    background: var(--soil-brown);
    display: flex; align-items: center;
    padding-left: 50px;
  }
  .tree-icons { width: 82px; height: 66px; background: var(--white); border-radius: 40px 40px 6px 6px; opacity: 0.95; }
  .offer {
    margin-left: 8px;
    font-weight: 700;
    font-size: 27px;
    line-height: 29px;
    letter-spacing: 0.3px;
  }
  .phone-icon { margin-left: 10px; width: 46px; height: 46px; }
  .phone-numbers {
    margin-left: 6px;
    font-family: "Anton", "Impact", sans-serif;
    font-size: 56px;
    letter-spacing: 0.3px;
    white-space: nowrap;
  }
  .tool-icons { margin-left: 12px; width: 130px; height: 66px; background: var(--white); border-radius: 4px; opacity: 0.95; }
</style>
</head>
<body>
<main class="flyer">
  <div class="hedge-photo" role="img" aria-label="Photograph of a neatly trimmed green hedge top against the sky"></div>

  <div class="brand-block">
    <div class="brand-art" role="img" aria-label="Illustration of bright green leaves behind a white picket fence"></div>
    <div class="brand-name">Bramblewick</div>
  </div>

  <h1 class="headline">Call your local, trusted and reliable Gardening Service</h1>

  <ul class="services services-left">
    <li>Lawn mowing</li>
    <li>One-off garden tidy ups or regular fortnightly visits</li>
    <li>All kinds of trees expertly felled, topped or pruned</li>
  </ul>

  <ul class="services services-right">
    <li>Hedge cutting</li>
    <li>Fencing replaced or repaired</li>
    <li>Fully insured</li>
    <li>Access to fully qualified and licenced tree arborist</li>
  </ul>

  <footer class="contact-bar">
    <div class="tree-icons" role="img" aria-label="Small white tree silhouettes"></div>
    <p class="offer">FREE QUOTES<br>FREE ADVICE</p>
    <svg class="phone-icon" viewBox="0 0 48 48" aria-hidden="true">
      <path d="M6 16c0-5 8-9 18-9s18 4 18 9v4h-9v-4c-2-1-5-2-9-2s-7 1-9 2v4H6z" fill="var(--white)"/>
      <path d="M14 22h20l6 16H8z" fill="var(--white)"/>
      <circle cx="24" cy="30" r="4" fill="var(--soil-brown)"/>
    </svg>
    <p class="phone-numbers">07724 316048 or 01632 742918</p>
    <div class="tool-icons" role="img" aria-label="White picket fence and lawn mower silhouettes"></div>
  </footer>
</main>
</body>
</html>
```